Business Card Design Competition

We need a business card design for our Internet Marketing company. We require both front and back designs and the final card must be 89x53mm in size, plus crop marks to 91x55mm. Colours as per logo, plus perhaps black and/or grey (#828282).
Final text must be editable (if you can supply an editable Fireworks PNG, even better)...
FRONT TEXT:
Full Name
Position
Address Line
Suburb, State, Postcode
Phone: 0000 000 000
Mobile: 0000 000 000
Email: xxx@brindlereach.com.au
Web: www.brindlereach.com.au
Rear of card should be a fresh design plus our slogan text: "Putting You Forward" in large font, then in small text "Brindle Harbour Pty Ltd (ABN: 42 356 701 483)".

```html
<!DOCTYPE html>
<html lang="en">
<head>
<meta charset="utf-8">
<title>Brindle Reach – Business Card</title>
<link rel="stylesheet" href="https://fonts.googleapis.com/css2?family=Open+Sans:ital,wght@0,400;0,600;0,700;1,600&display=swap">
<style>
  :root {
    --backdrop: #e6e4e0;
    --card-dark: #1c1c1c;
    --card-mid: #2e2e2e;
    --green: #8cc63f;
    --green-light: #c6e36a;
    --green-deep: #3d6b12;
    --amber: #f0b52c;
    --text-light: #e4e4e4;
    --grey: #828282;
  }
  * { margin: 0; padding: 0; box-sizing: border-box; }
  html, body { width: 1200px; height: 871px; overflow: hidden; }
  body {
    background: var(--backdrop);
    font-family: "Open Sans", Arial, sans-serif;
    position: relative;
  }
  .card {
    position: absolute;
    top: 100px;
    width: 400px;
    height: 672px;
    background: radial-gradient(ellipse at 50% 45%, var(--card-mid), var(--card-dark) 75%);
    overflow: hidden;
    box-shadow: 0 10px 30px rgba(0,0,0,0.25);
  }
  .card--front { left: 170px; }
  .card--back { left: 630px; }
  .swoosh { position: absolute; left: 0; width: 100%; }
  .swoosh--top { top: 0; height: 190px; }
  .swoosh--bottom { bottom: 0; height: 150px; }
  .swoosh--side { top: 0; height: 100%; }

  .brand {
    position: absolute;
    top: 215px;
    left: 40px;
    display: flex;
    align-items: center;
    gap: 14px;
  }
  .brand__dot {
    width: 54px; height: 54px;
    border-radius: 50%;
    background: var(--green);
  }
  .brand__name {
    font-size: 32px;
    font-weight: 600;
    color: var(--green);
    line-height: 1;
  }
  .contact {
    position: absolute;
    left: 0; right: 0;
    top: 300px;
    text-align: center;
    color: var(--text-light);
    font-size: 17px;
    line-height: 1.3;
  }
  .contact__name {
    font-size: 34px;
    font-weight: 700;
    line-height: 1;
    letter-spacing: 0.5px;
  }
  .contact__name .first { color: var(--green); }
  .contact__name .last { color: var(--amber); }
  .contact__title { font-size: 18px; margin-bottom: 30px; }
  .contact__address { margin-bottom: 14px; }
  .contact__lines { margin-bottom: 22px; }
  .label--green { color: var(--green); }
  .label--amber { color: var(--amber); }
  .contact__web { font-size: 17px; }

  .slogan {
    position: absolute;
    left: 200px;
    top: 336px;
    width: 560px;
    transform: translate(-50%, -50%) rotate(-90deg);
    text-align: center;
  }
  .slogan__line {
    font-size: 38px;
    font-weight: 600;
    font-style: italic;
    color: var(--green);
    line-height: 1.1;
  }
  .slogan__legal {
    font-size: 14px;
    color: var(--text-light);
    margin-top: 8px;
  }
</style>
</head>
<body>

<section class="card card--front" aria-label="Card front">
  <svg class="swoosh swoosh--top" viewBox="0 0 400 190" preserveAspectRatio="none" aria-hidden="true">
    <defs>
      <linearGradient id="frontTop" x1="0" y1="0" x2="1" y2="1">
        <stop offset="0" stop-color="#8cc63f"/>
        <stop offset="0.5" stop-color="#c6e36a"/>
        <stop offset="1" stop-color="#3d6b12"/>
      </linearGradient>
    </defs>
    <path d="M0 0 H400 V120 C300 60 140 70 0 150 Z" fill="url(#frontTop)" opacity="0.85"/>
    <path d="M0 0 H400 V70 C290 20 140 60 0 110 Z" fill="#3d6b12" opacity="0.6"/>
    <path d="M0 150 C140 70 300 60 400 120 V130 C300 80 140 90 0 165 Z" fill="#c6e36a" opacity="0.5"/>
  </svg>

  <div class="brand">
    <span class="brand__dot"></span>
    <span class="brand__name">Brindle Reach</span>
  </div>

  <div class="contact">
    <p class="contact__name"><span class="first">ALEX</span> <span class="last">MARLOW</span></p>
    <p class="contact__title">Special Job Title</p>
    <p class="contact__address">Address Line<br>Suburb, State, Postcode</p>
    <p class="contact__lines"><span class="label--green">Phone:</span> 0000 000 000<br><span class="label--green">Mobile:</span> 0000 000 000</p>
    <p class="contact__web"><span class="label--amber">Email:</span> xxx@brindlereach.com.au<br><span class="label--amber">Web:</span> www.brindlereach.com.au</p>
  </div>

  <svg class="swoosh swoosh--bottom" viewBox="0 0 400 150" preserveAspectRatio="none" aria-hidden="true">
    <defs>
      <linearGradient id="frontBottom" x1="0" y1="0" x2="1" y2="1">
        <stop offset="0" stop-color="#3d6b12"/>
        <stop offset="0.5" stop-color="#c6e36a"/>
        <stop offset="1" stop-color="#8cc63f"/>
      </linearGradient>
    </defs>
    <path d="M0 80 C120 40 280 30 400 70 V150 H0 Z" fill="url(#frontBottom)" opacity="0.85"/>
    <path d="M0 110 C140 70 280 80 400 110 V150 H0 Z" fill="#3d6b12" opacity="0.6"/>
    <path d="M0 80 C120 40 280 30 400 70 V78 C280 42 120 52 0 90 Z" fill="#c6e36a" opacity="0.6"/>
  </svg>
</section>

<section class="card card--back" aria-label="Card back">
  <svg class="swoosh swoosh--side" viewBox="0 0 400 672" preserveAspectRatio="none" aria-hidden="true">
    <defs>
      <linearGradient id="backTop" x1="0" y1="0" x2="1" y2="1">
        <stop offset="0" stop-color="#8cc63f"/>
        <stop offset="1" stop-color="#3d6b12"/>
      </linearGradient>
      <linearGradient id="backSide" x1="0" y1="0" x2="1" y2="0">
        <stop offset="0" stop-color="#3d6b12"/>
        <stop offset="0.6" stop-color="#c6e36a"/>
        <stop offset="1" stop-color="#8cc63f"/>
      </linearGradient>
    </defs>
    <path d="M0 0 H60 C40 60 20 120 0 170 Z" fill="url(#backTop)" opacity="0.85"/>
    <path d="M400 300 C320 380 300 520 330 672 H400 Z" fill="url(#backSide)" opacity="0.85"/>
    <path d="M400 360 C350 430 340 540 360 672 H400 Z" fill="#3d6b12" opacity="0.6"/>
    <path d="M400 300 C320 380 300 520 330 672 H338 C310 520 330 385 400 312 Z" fill="#c6e36a" opacity="0.6"/>
  </svg>

  <div class="slogan">
    <p class="slogan__line">Putting You Forward</p>
    <p class="slogan__legal">Brindle Harbour Pty Ltd (ABN: 42 356 701 483)</p>
  </div>
</section>

</body>
</html>
```